Fenwistrakes meets Morvanta

Hello,

at first, please excuse my not percfect english, i'am from germany! :)

I have coded a .php-based website, this website is about mixing several things like chocolate, wine gums or little toys together and send them in a "tube" to the buyer adress or to a adress the buyer chose to suprise somebody.

A part of the revenue of every sold "tube", i want to give to german charity.

Please check uploaded pictures:

1.jpg: on this picture you see the mainsite. on the left side you see the "tube". This "tube" will be filled with the different things which will be chosed by user. Below the "tube" you will see the price and the quantity of fillable space in the "tube" in gramms. The user can chose "L", "XL" and "XXL", with this chose the user specific the high of the tube. On the right side you see the main menu, the user can now chose the different category, beginning from the top: gift wrap, chocolate, miscellaneous, the billing adress, the delivery adress and at last the order button.

around are little buttons like "tube", "how it works", "about us" etc.

2.jpg: here you see the "tubes", this "tubes" filled with chocolate or something else will be sended to user. You can see that the mainsite is in the middle window, if you click on a button, the window in the middle will change

3.jpg: here you can see the window if the user chose "chocolate" to pick some several chocolate to fill in the "tube"

To be honest iam still not sure in which direction i want to go, i like selfdrawed icons, modern look, but i think pictures for exampleof chocolate are also really cool! i think i want to have a modern-drawed-lovely-design with the charity-think (remember i will spent money for kids from the revenue of each sold "tube")!

I coded this website with .php, the outlines and grafics are .css based! i like the positions of each window and button, but of course i can change every width and hight of every field you see and of course i can move them or add new one.

Target Market(s)

people who want to spent money with buying something

Requirements
Must have
• - a logo, the website is called "pilnorax.de" (perhaps with a "tube" within)
- a painted or 3d-designed "tube" (filled with 1 thing to 100%, filled with 2 things each 50%, filled with 3 things each 33%, filled with 4 things each 25%, filled with 5 things each 20%) the user can chose up to 5 different things to fill in the "tube", if he chose for example 2 things, the "tube" on the left change to a tube filled with 2 things
- 4 different gift wrap layers (standard, christmas theme, birthday theme, neutral theme, eastern theme) this layer will be layed over the "tube" on the left if user chose one of them
- the right menue (6 "buttons" or pictures)
- perhaps a background for each category: gift wrap, chocolate, miscellaneous, billing adress, delivery adress order button.
- main background

```html
<!DOCTYPE html>
<html lang="en">
<head>
<meta charset="utf-8">
<title>Pilnorax – Welcome</title>
<link href="https://fonts.googleapis.com/css2?family=Cabin:wght@400;500&family=Arimo&family=Noto+Serif&family=Rosario&display=swap" rel="stylesheet">
<style>
  :root{
    --page:#ffffff;
    --header-bg:#ececec;
    --purple-top:#a04fae;
    --purple-bottom:#7f3590;
    --magenta-top:#d02fa9;
    --magenta-bottom:#a6117e;
    --pink-label:#f47fbb;
    --heading:#8c2a8c;
    --body-text:#2b2b2b;
    --dark-top:#3b3b3b;
    --dark-bottom:#050505;
    --footer-bar:#141414;
    --footer-text:#9a9a9a;
    --tile-border:#d6d6d6;
    --logo:#ee6f1e;
    --product-dark:#3a2f33;
    --product-mid:#5e4c50;
  }
  *{box-sizing:border-box;margin:0;padding:0}
  html,body{width:1200px;height:887px;overflow:hidden;background:var(--page)}
  .canvas{position:relative;width:1200px;height:887px;font-family:"Arimo",Arial,sans-serif}

  .header-band{position:absolute;left:0;top:0;width:1200px;height:162px;background:var(--header-bg)}
  .header-band::after{content:"";position:absolute;left:0;bottom:-5px;width:100%;height:6px;
    background:linear-gradient(135deg,var(--header-bg) 50%,transparent 50%) 0 0/6px 6px repeat-x,
               linear-gradient(225deg,var(--header-bg) 50%,transparent 50%) 0 0/6px 6px repeat-x}
  .header-band::before{content:"";position:absolute;left:0;top:0;width:100%;height:4px;
    background:linear-gradient(45deg,#fff 50%,transparent 50%) 0 0/6px 6px repeat-x,
               linear-gradient(-45deg,#fff 50%,transparent 50%) 0 0/6px 6px repeat-x}

  .logo{position:absolute;left:178px;top:22px;font-family:"Cabin",sans-serif;font-weight:500;font-size:42px;color:var(--logo);letter-spacing:-.5px}
  .social{position:absolute;left:869px;top:35px;display:flex;gap:11px}
  .social span{width:22px;height:22px;border-radius:3px;display:block}

  .main-nav{position:absolute;left:177px;top:91px;width:845px;height:53px;
    background:linear-gradient(var(--purple-top),var(--purple-bottom));border:1px solid #6e2c80;display:flex}
  .main-nav a,.foot-nav a{color:#fff;text-decoration:none;font-family:"Cabin",sans-serif;font-size:14px;
    display:flex;align-items:center;justify-content:center;position:relative}
  .main-nav a+a::before,.foot-nav a+a::before{content:"";position:absolute;left:0;top:11px;bottom:11px;width:1px;background:rgba(255,255,255,.3)}
  .main-nav a:nth-child(1){width:180px}.main-nav a:nth-child(2){width:166px}
  .main-nav a:nth-child(3){width:274px}.main-nav a:nth-child(4){width:225px}

  .product-visual{position:absolute;left:196px;top:187px;width:134px;height:368px;
    background:linear-gradient(180deg,var(--product-mid),var(--product-dark))}
  .price{position:absolute;left:177px;top:570px;width:160px;text-align:center;font-size:10.5px;line-height:20.5px;color:#222}
  .sizes{position:absolute;left:177px;top:646px;display:flex;gap:2px}
  .sizes span{width:52px;height:53px;border:1px solid #8e0f6d;background:linear-gradient(var(--magenta-top),var(--magenta-bottom));
    color:#fff;font-family:"Cabin",sans-serif;font-size:22px;display:flex;align-items:center;justify-content:center}

  .slider{position:absolute;left:355px;top:185px;width:453px;height:185px;border:1px solid #ccc;
    background:linear-gradient(135deg,#8a5a44,#c6ab8c 50%,#4a2a1e)}
  .dots{position:absolute;right:12px;bottom:6px;display:flex;gap:3px}
  .dots i{width:8px;height:8px;border-radius:50%;background:#7b1f6b}
  .dots i:first-child{background:#e9589f}

  .welcome{position:absolute;left:355px;top:386px;font-family:"Rosario",sans-serif;font-weight:400;font-size:17px;color:var(--heading)}
  .intro{position:absolute;left:358px;top:416px;width:358px;font-family:"Noto Serif",serif;font-size:10px;line-height:20.3px;color:var(--body-text);text-align:justify}
  .intro p+p{margin-top:20.3px}

  .thumbs{position:absolute;left:355px;top:693px;height:92px}
  .thumb{position:absolute;top:0;height:92px;border:1px solid var(--tile-border)}
  .terms{position:absolute;left:13px;bottom:5px;font-size:9.5px;line-height:13.5px;color:#333}

  .menu-tile{position:absolute;left:818px;width:204px;height:93px;border:1px solid var(--tile-border)}
  .menu-tile span{position:absolute;right:1px;bottom:9px;background:var(--pink-label);color:#3a1030;font-size:13px;padding:3px 4px 3px 16px;text-transform:uppercase}

  .foot-nav{position:absolute;left:177px;top:797px;width:845px;height:52px;background:linear-gradient(var(--dark-top),var(--dark-bottom));display:flex}
  .foot-nav a:nth-child(1){width:203px}.foot-nav a:nth-child(2){width:202px}
  .foot-nav a:nth-child(3){width:308px}.foot-nav a:nth-child(4){width:132px}
  .copyright{position:absolute;left:0;top:854px;width:1200px;height:33px;background:var(--footer-bar);color:var(--footer-text);
    font-size:10.5px;display:flex;align-items:center;justify-content:center;gap:20px}
</style>
</head>
<body>
<div class="canvas">
  <div class="header-band"></div>
  <div class="logo">Pilnorax</div>
  <div class="social" aria-label="Social networks">
    <span style="background:#3b5998"></span><span style="background:#45b7e8"></span>
    <span style="background:#1f7ab5"></span><span style="background:#f08a1c"></span><span style="background:#d9453a"></span>
  </div>

  <nav class="main-nav">
    <a href="#">The Tubes</a><a href="#">How it works</a>
    <a href="#">Dos Morvanta Children's Funds</a><a href="#">What I Pilnorax.de</a>
  </nav>

  <div class="product-visual" role="img" aria-label="Product image: tube filled with assorted chocolates"></div>
  <div class="price">Approximately<br>430 grams = 16.90 euros<br>tv WST UNCL Shipping</div>
  <div class="sizes"><span>L</span><span>XL</span><span>XXL</span></div>

  <div class="slider" role="img" aria-label="Close-up photo of assorted chocolate pralines">
    <div class="dots"><i></i><i></i><i></i><i></i></div>
  </div>

  <h1 class="welcome">WELCOME LIERZLICH</h1>
  <div class="intro">
    <p>On Pilnorax.de brought to you by putting together a selection of toys and SliBigkeiten and leave this choice to send in a so-called tube.</p>
    <p>How this works is you can learn here ...</p>
    <p>Of the revenue of each sent Tube, Pilnorax.de donates each 1, - Euro to the Morvanta Children's Fund</p>
    <p>Previous donations: 2345 Euro</p>
    <p>current Clberweisungsbeled</p>
    <p>Thank you,</p>
  </div>

  <div class="thumbs">
    <div class="thumb" style="left:0;width:94px;background:linear-gradient(135deg,#e8c23a,#d8453c 50%,#6bb04a)" role="img" aria-label="Colourful gummy sweets"></div>
    <div class="thumb" style="left:97px;width:94px;background:linear-gradient(#4a3028,#cdbfb3 55%,#f2eeea)" role="img" aria-label="Cup of cream dessert"></div>
    <div class="thumb" style="left:194px;width:94px;background:linear-gradient(135deg,#6b3a22,#a8704a 50%,#4b2616)" role="img" aria-label="Milk chocolate pralines"></div>
    <div class="thumb" style="left:291px;width:162px;background:linear-gradient(135deg,#e7dccb,#c9b99f 55%,#9ea2a8)" role="img" aria-label="Paper scroll and parchment">
      <div class="terms">I accept the Terms and<br>Conditions of pilnorax.de</div>
    </div>
  </div>

  <div class="menu-tile" style="top:185px;background:linear-gradient(135deg,#f7f2ec,#c7a97a 50%,#f5f1ee)" role="img" aria-label="Wrapped gift box with blue bow"><span>Gift Warp</span></div>
  <div class="menu-tile" style="top:286px;background:linear-gradient(135deg,#d8357a,#3a2a22 50%,#e46aa5)" role="img" aria-label="Chocolate cupcake and candies"><span>Chocolate</span></div>
  <div class="menu-tile" style="top:388px;background:linear-gradient(135deg,#e28a2a,#b55a1a 50%,#f0a64a)" role="img" aria-label="Dried fruits"><span>Miscellaneous</span></div>
  <div class="menu-tile" style="top:489px;background:linear-gradient(135deg,#f4ede6,#d8b49a 45%,#3a3a3a)" role="img" aria-label="Hands with calculator and pen"><span>Billing Address</span></div>
  <div class="menu-tile" style="top:591px;background:linear-gradient(135deg,#d8d0c0,#2e7fc8 55%,#d4b454)" role="img" aria-label="Toy airplane on envelopes"><span>Shipping Address</span></div>
  <div class="menu-tile" style="top:692px;background:linear-gradient(135deg,#ffffff,#f3ece7 60%,#c9c3bd)" role="img" aria-label="Hand pressing a service bell"><span>Order</span></div>

  <nav class="foot-nav">
    <a href="#">Social Networks</a><a href="#">General Policy</a>
    <a href="#">Imprint / Terms and conditions</a><a href="#">Home</a>
  </nav>
  <div class="copyright"><span>Copyright © 2012 Pilnorax, All Rights Reserved</span><span>M3</span></div>
</div>
</body>
</html>
```